Landscape install that wants to be known for specializing in backyard oasis

I install high end backyard retreats, I also instal water features, kitchens, patio and plants, I am not a landscaper that cuts grass for a source of income but I want to be know as someone who could be the first company you think of when you want any form of hard scape installed. Up to this point my projects have required a creative custom install that is different to cookie cutter install companies, I chose the name to reflect a company that is professional but also let customer know that I work and specialize in stone install

Target Market(s)

To everyone but more important is target customers and professionals that my company is the one they should choose

Industry/Entity Type

Landscape

Contact Information for Business Card

Martin Keswick
2847 Thornbury Dr
Wrenhollow, IL 60482
Email: www.bramblestoneworks@mailvane.com

Requirements
Must have
• If you could help with a signature logo or something current and relevant
Nice to have
• Creative layout of the card with an great backdrop that reflects the company as cutting edge and current

```html
<!DOCTYPE html>
<html lang="en">
<head>
<meta charset="utf-8">
<title>Bramblestone Works – Business Card</title>
<link href="https://fonts.googleapis.com/css2?family=Arimo:wght@400;700&display=swap" rel="stylesheet">
<style>
  :root {
    --page-bg: #ffffff;
    --card-light-top: #ffffff;
    --card-light-bottom: #e6e6e6;
    --ink-dark: #2a2a2a;
    --mark-grey: #5a5a5a;
    --band-light: #f2f2f2;
    --band-mid: #a9a9a9;
    --band-dark: #6e6e6e;
    --panel-dark: #3c3c3c;
    --panel-mid: #555555;
    --text-light: #f4f4f4;
    --text-soft: #c9c9c9;
    --icon-grey: #9a9a9a;
  }
  * { box-sizing: border-box; margin: 0; padding: 0; }
  html, body {
    width: 1200px; height: 900px; overflow: hidden;
    background: var(--page-bg);
    font-family: "Arimo", Arial, sans-serif;
  }
  .canvas { position: relative; width: 1200px; height: 900px; }

  .card {
    position: absolute; top: 300px;
    width: 520px; height: 300px;
    border-radius: 20px; overflow: hidden;
    box-shadow: 0 10px 28px rgba(0,0,0,0.22);
  }
  .card--front { left: 50px; }
  .card--back { left: 630px; }

  /* front: header */
  .front-header {
    position: absolute; left: 0; top: 0; width: 100%; height: 136px;
    background: linear-gradient(180deg, var(--card-light-top), var(--card-light-bottom));
  }
  .brand {
    position: absolute; left: 24px; top: 48px;
    display: flex; align-items: center; gap: 16px;
  }
  .brand-square { width: 44px; height: 44px; background: var(--mark-grey); }
  .brand-name {
    font-size: 27px; font-weight: 700; color: var(--ink-dark); letter-spacing: 0.01em;
    white-space: nowrap;
  }

  /* front: tagline band */
  .tagline-band {
    position: absolute; left: 0; top: 136px; width: 100%; height: 18px;
    background: linear-gradient(90deg, var(--band-dark), var(--band-light) 45%, var(--band-mid) 80%, var(--band-light));
    display: flex; align-items: center; justify-content: center;
  }
  .tagline {
    font-size: 11px; letter-spacing: 0.9em; color: var(--ink-dark); text-transform: uppercase;
    white-space: nowrap;
  }

  /* front: dark details panel */
  .details-panel {
    position: absolute; left: 0; top: 154px; width: 100%; height: 146px;
  }
  .panel-texture {
    position: absolute; inset: 0;
    background: linear-gradient(160deg, var(--panel-mid), var(--panel-dark));
  }
  .contact-name {
    position: absolute; left: 20px; top: 18px;
    font-size: 17px; color: var(--text-soft);
  }
  .contact-line {
    position: absolute; left: 20px;
    display: flex; align-items: center; gap: 6px;
    font-size: 15px; color: var(--text-light); white-space: nowrap;
  }
  .contact-line--phone { top: 70px; }
  .contact-line--address { top: 96px; }
  .contact-icon { width: 13px; height: 13px; fill: var(--icon-grey); }

  /* back */
  .back-texture {
    position: absolute; inset: 0;
    background: linear-gradient(160deg, var(--panel-mid), var(--panel-dark));
  }
  .back-brand {
    position: absolute; inset: 0;
    display: flex; align-items: center; justify-content: center; gap: 16px;
  }
  .back-brand .brand-square { width: 40px; height: 40px; background: var(--text-soft); }
  .back-brand .brand-name { color: var(--text-soft); font-size: 30px; }
</style>
</head>
<body>
<main class="canvas">

  <section class="card card--front">
    <header class="front-header">
      <div class="brand">
        <div class="brand-square"></div>
        <span class="brand-name">Bramblestone Works</span>
      </div>
    </header>
    <div class="tagline-band"><span class="tagline">Shaped in solid stone</span></div>
    <div class="details-panel">
      <div class="panel-texture" role="img" aria-label="Dark perforated metal texture"></div>
      <p class="contact-name">Martin Keswick</p>
      <p class="contact-line contact-line--phone">
        <svg class="contact-icon" viewBox="0 0 24 24" aria-hidden="true"><path d="M6.6 10.8a15.1 15.1 0 0 0 6.6 6.6l2.2-2.2a1 1 0 0 1 1-.25 11.4 11.4 0 0 0 3.6.57 1 1 0 0 1 1 1V20a1 1 0 0 1-1 1A17 17 0 0 1 3 4a1 1 0 0 1 1-1h3.5a1 1 0 0 1 1 1c0 1.25.2 2.45.57 3.6a1 1 0 0 1-.25 1z"/></svg>
        1472 903 518
      </p>
      <p class="contact-line contact-line--address">
        <svg class="contact-icon" viewBox="0 0 24 24" aria-hidden="true"><path d="M12 3 2 12h3v8h5v-6h4v6h5v-8h3z"/></svg>
        2847 Thornbury Dr Wrenhollow, IL 60482
      </p>
    </div>
  </section>

  <section class="card card--back">
    <div class="back-texture" role="img" aria-label="Dark perforated metal texture"></div>
    <div class="back-brand">
      <div class="brand-square"></div>
      <span class="brand-name">Bramblestone Works</span>
    </div>
  </section>

</main>
</body>
</html>
```